Product label for premium fruit wooden crates

Background: Kiralo offers premium quality fruits airflown (i.e. Japan, USA, Australia, etc) to Singapore at an affordable price. This includes exquisite and limited fruits like Shine Muscat grape, Shizuoka Ember Melon, Yellow Dragon Fruit, Fei zi xiao seedless lychee, Yellow Peaches, etc.

Requirements:

- Design a premium fruit’s label strap for identification and brand marketing.

- This strap will be used to tie around our fruit gift crate and fruit boxes (see attached).

- the logo use in this strap may use different color that must fit the 2 ribbons that will be used together with the crate box (see attached), red and gold ribbons(purl satin)

- the fruit crates and boxes will be presented as gift for vip, families, and working partners (important people)

This label will be printed in paper and tie around the fruit crate or paper box.

Web: www.kiralo.sg
FB: https://www.pagenest.net/krlorchard/
IG: https://www.snapgrid.net/krlorchard

Target Market(s)

Working class, families, expat, business clients (late 20 – 40s)

Industry/Entity Type

Gift Shop

Other font styles liked:
• Sakkal Majalla

Requirements
Must have
• - color that fit the 2 ribbons color (red and gold)
• - premium, luxury and exquisite feel
• - presentable as a gift to someone important
• - Kiralo's logo
• - The word 'KIRALO',
Nice to have
• the following words:
• - www.kiralo.sg; or/and
• - online premium fruits or/and
• - premium quality (No preference. let the designer choose)
• must be able to give customer a feel that Kiralo sells premium fruits
Should not have
• cant think of it now

```html
<!DOCTYPE html>
<html lang="en">
<head>
<meta charset="utf-8">
<title>Kiralo — Fruit Crate Label Strap</title>
<link href="https://fonts.googleapis.com/css2?family=Montserrat:wght@300;400&display=swap" rel="stylesheet">
<style>
  :root {
    --paper: #ffffff;
    --strap-red: #ec1c24;
    --strap-red-deep: #c71f2d;
    --gold: #e9c46e;
    --gold-light: #f6dc9a;
    --gold-deep: #c99a3e;
  }
  * { margin: 0; padding: 0; box-sizing: border-box; }
  html, body {
    width: 1200px;
    height: 459px;
    overflow: hidden;
    background: var(--paper);
  }
  .canvas {
    position: relative;
    width: 1200px;
    height: 459px;
    background: var(--paper);
    font-family: "Montserrat", sans-serif;
  }

  .strap {
    position: absolute;
    overflow: hidden;
    background: var(--strap-red);
  }
  .strap-pattern {
    position: absolute;
    inset: 0;
    background:
      radial-gradient(ellipse 9% 60% at 12% 40%, rgba(199,31,45,.75), transparent 70%),
      radial-gradient(ellipse 9% 60% at 40% 55%, rgba(199,31,45,.6), transparent 70%),
      radial-gradient(ellipse 9% 60% at 68% 40%, rgba(199,31,45,.7), transparent 70%),
      radial-gradient(ellipse 9% 60% at 92% 55%, rgba(199,31,45,.75), transparent 70%),
      linear-gradient(90deg, var(--strap-red), var(--strap-red-deep) 50%, var(--strap-red));
    opacity: .85;
  }
  .gold-rule {
    position: absolute;
    left: 0;
    right: 0;
    background: linear-gradient(90deg, var(--gold-light), var(--gold) 40%, var(--gold-deep) 75%, var(--gold-light));
  }

  .brand {
    position: absolute;
    display: flex;
    align-items: center;
    color: var(--gold);
  }
  .brand-dot {
    flex: none;
    border-radius: 50%;
    background: var(--gold);
  }
  .brand-words { display: flex; flex-direction: column; line-height: 1; }
  .brand-name { font-weight: 300; }
  .brand-tagline { font-weight: 400; }

  /* Narrow strap */
  .strap--narrow { left: 64px; top: 8px; width: 1068px; height: 44px; }
  .strap--narrow .gold-rule--top { top: 5px; height: 2px; }
  .strap--narrow .gold-rule--bottom { top: 37px; height: 2px; }
  .strap--narrow .brand { top: 10px; }
  .strap--narrow .brand-dot { width: 19px; height: 19px; margin-right: 5px; }
  .strap--narrow .brand-name { font-size: 16px; letter-spacing: 1.5px; }
  .strap--narrow .brand-tagline { font-size: 6.5px; letter-spacing: .3px; margin-top: 1px; }

  /* Wide strap */
  .strap--wide { left: 0; top: 287px; width: 1200px; height: 146px; }
  .strap--wide .gold-rule--top { top: 15px; height: 6px; }
  .strap--wide .gold-rule--bottom { top: 125px; height: 6px; }
  .strap--wide .brand { left: 392px; top: 30px; }
  .strap--wide .brand-dot { width: 70px; height: 70px; margin-right: 36px; }
  .strap--wide .brand-name { font-size: 62px; letter-spacing: 5px; }
  .strap--wide .brand-tagline { font-size: 19px; letter-spacing: 3.2px; margin-top: 4px; }
</style>
</head>
<body>
<main class="canvas">

  <section class="strap strap--narrow" aria-label="Narrow crate strap">
    <div class="strap-pattern" role="img" aria-label="Dark red ornamental swirl pattern"></div>
    <div class="gold-rule gold-rule--top"></div>
    <div class="gold-rule gold-rule--bottom"></div>
    <div class="brand" style="left:56px">
      <span class="brand-dot"></span>
      <span class="brand-words"><span class="brand-name">KIRALO</span><span class="brand-tagline">ONLINE PREMIUM FRUITS</span></span>
    </div>
    <div class="brand" style="left:324px">
      <span class="brand-dot"></span>
      <span class="brand-words"><span class="brand-name">KIRALO</span><span class="brand-tagline">ONLINE PREMIUM FRUITS</span></span>
    </div>
    <div class="brand" style="left:592px">
      <span class="brand-dot"></span>
      <span class="brand-words"><span class="brand-name">KIRALO</span><span class="brand-tagline">ONLINE PREMIUM FRUITS</span></span>
    </div>
    <div class="brand" style="left:860px">
      <span class="brand-dot"></span>
      <span class="brand-words"><span class="brand-name">KIRALO</span><span class="brand-tagline">ONLINE PREMIUM FRUITS</span></span>
    </div>
  </section>

  <section class="strap strap--wide" aria-label="Wide crate strap">
    <div class="strap-pattern" role="img" aria-label="Dark red ornamental swirl pattern"></div>
    <div class="gold-rule gold-rule--top"></div>
    <div class="gold-rule gold-rule--bottom"></div>
    <div class="brand">
      <span class="brand-dot"></span>
      <span class="brand-words"><span class="brand-name">KIRALO</span><span class="brand-tagline">ONLINE PREMIUM FRUITS</span></span>
    </div>
  </section>

</main>
</body>
</html>
```